Designing a website that functions as the shop window for the various aspects of my business -...

I need a website, with separate webpages covering the different components of my practice (small animal consultancy, equine behaviour consultancy, legal case work and education provider). I have a website (www.petmindstudio.ie) but I haven't updated it in recent years to reflect the newer developments / aspects of my business. Most of my work has been in Ireland but I would like to begin to create an international profile, particularly with regard to the legal casework and offering education within the international horse industry. My overall goal is to improve understanding of animals and animal behaviour, and by doing so, help to reduce the performance of behaviour problems, and also improve animal welfare as a result.

Target Market(s)

Horse and dog owners, horse riders, veterinary surgeons, solicitors

Industry/Entity Type

Legal

Logo Text

Text to be decided on

Number of Pages Required

5+ page

Font styles to use
Sans Serif
Decorative
Script

Colors

Designer to choose colors to be used in the design.

Requirements
Must have
• Relevant content from the attached Flyer including photos
• Use of the phrases:
• 'Understanding Animals'
• Improving animals lives through better understanding
• Science-based, up-to-date relevant information regarding animal behaviour
Nice to have
• 'Leading professional service educating people in understanding animals'
• Separate pages for 1) About, 2) Canine and Feline behaviour Consultancy 3) Equine Consultancy 4) Legal expert witness Consultancy 5) Education 6, FAQs
Should not have
• Prices of services (as these may change from time to time)

```html
<!DOCTYPE html>
<html lang="en">
<head>
<meta charset="utf-8">
<title>PetMind Studio – Equine Training, Performance &amp; Welfare</title>
<link href="https://fonts.googleapis.com/css2?family=Montserrat:wght@400;500;600&family=Open+Sans:ital,wght@0,400;0,600;0,700;1,400&display=swap" rel="stylesheet">
<style>
:root{
  --green:#1c8a4c;
  --green-dark:#146b39;
  --mint:#e4f3ee;
  --ink:#2b2b2b;
  --muted:#6f6f6f;
  --line:#d9d9d9;
  --white:#ffffff;
}
*{box-sizing:border-box;margin:0;padding:0}
html,body{width:1200px;height:4390px;overflow:hidden;background:var(--white)}
body{position:relative;font-family:"Open Sans",Arial,sans-serif;color:var(--ink)}
.abs{position:absolute}
h2.section-title{position:absolute;left:0;width:1200px;text-align:center;font-family:"Montserrat",Arial,sans-serif;font-weight:500;font-size:42px;color:#222}
.rule{position:absolute;left:540px;width:120px;height:5px;background:var(--green)}
.lead{position:absolute;left:190px;width:820px;text-align:center;font-size:15px;line-height:30px;color:var(--muted)}

/* header */
.brand{left:112px;top:24px;display:flex;align-items:center;gap:16px}
.brand-mark{width:46px;height:46px;border-radius:50%;background:var(--green)}
.brand-name{font-family:"Montserrat",Arial,sans-serif;font-weight:600;font-size:36px;color:var(--green)}
.call{left:860px;top:20px;display:flex;align-items:center;gap:16px}
.call-icon{width:50px;height:50px;border-radius:50%;border:2px solid #cfcfcf;display:flex;align-items:center;justify-content:center}
.call small{display:block;font-size:16px;color:#333}
.call strong{display:block;font-family:"Montserrat",Arial,sans-serif;font-size:27px;font-weight:600;color:#222}
.nav{left:112px;top:120px;display:flex;gap:22px;font-size:15px;color:#333}
.nav .active{color:var(--green)}
.nav-line{left:0;top:152px;width:1200px;height:1px;background:var(--line)}

/* hero */
.hero{left:0;top:158px;width:1200px;height:590px;background:linear-gradient(90deg,#2d6b2c 0%,#6d8f3a 40%,#b88a4a 70%,#9c6a33 100%)}
.hero-title{left:108px;top:220px;font-family:"Montserrat",Arial,sans-serif;font-size:48px;font-weight:500;line-height:64px;color:var(--white)}
.hero-rule{left:108px;top:370px;width:530px;height:4px;background:var(--white)}
.hero-list{left:108px;top:400px;list-style:none;color:var(--white);font-size:18px;font-weight:600}
.hero-list li{position:relative;padding-left:32px;margin-bottom:28px;line-height:28px;width:460px}
.hero-list li svg{position:absolute;left:0;top:4px}
.btn-ghost{left:111px;top:615px;width:180px;height:58px;border:2px solid var(--white);border-radius:30px;color:var(--white);font-size:16px;font-weight:700;display:flex;align-items:center;justify-content:center}
.dots{left:566px;top:684px;display:flex;gap:6px}
.dots span{width:14px;height:14px;border-radius:50%;border:2px solid var(--white)}
.dots span.on{background:var(--white)}

/* services */
.svc-band{left:0;top:1180px;width:1200px;height:590px}
.svc-photo{position:absolute;width:222px;height:222px;border-radius:50%;border:6px solid var(--white);box-shadow:0 2px 10px rgba(0,0,0,.25)}
.svc{position:absolute;width:250px;text-align:center;color:var(--white)}
.svc h3{font-family:"Montserrat",Arial,sans-serif;font-weight:500;font-size:24px;line-height:33px}
.svc p{font-size:14px;line-height:24px;margin-top:14px}
.btn-svc{position:absolute;width:128px;height:47px;border:2px solid var(--white);border-radius:24px;color:var(--white);font-size:14px;font-weight:700;display:flex;align-items:center;justify-content:center}

/* components */
.components{left:0;top:1768px;width:1200px;height:594px;background:var(--mint)}
.comp-hub{left:483px;top:2002px;width:234px;height:234px;border-radius:50%;background:var(--green);display:flex;align-items:center;justify-content:center}
.comp-icon{position:absolute;width:94px;height:94px;border-radius:50%;background:var(--white);display:flex;align-items:center;justify-content:center;box-shadow:0 0 0 6px rgba(255,255,255,.5)}
.comp-label{position:absolute;width:320px}
.comp-label h4{font-family:"Montserrat",Arial,sans-serif;font-weight:500;font-size:19px;color:#222}
.comp-label p{font-size:14px;color:var(--muted);margin-top:8px}
.comp-label.right{text-align:right}

/* equine */
.byline{left:0;top:2562px;width:1200px;text-align:center;font-family:"Montserrat",Arial,sans-serif;font-weight:500;font-size:19px;color:#555}
.video{left:328px;top:2725px;width:544px;height:348px;background:linear-gradient(160deg,#3f6a2e 0%,#6e8f45 45%,#2f3a2a 100%)}
.play{left:568px;top:2867px;width:64px;height:64px;border-radius:50%;background:rgba(0,0,0,.6);display:flex;align-items:center;justify-content:center}

/* testimonials */
.testi{left:0;top:3179px;width:1200px;height:486px;background:linear-gradient(90deg,#d9ddd9 0%,#eceeec 50%,#dcdfdc 100%)}
.quote{left:170px;top:3376px;width:860px;text-align:center;font-style:italic;font-size:15.5px;line-height:34px;color:#555}
.cite{left:0;top:3546px;width:1200px;text-align:center;font-size:20px;font-weight:600;color:#333}
.arrow{top:3428px}

/* contact */
.col-title{font-family:"Montserrat",Arial,sans-serif;font-weight:500;font-size:25px;color:#222}
.field{position:absolute;border:1px solid #9a9a9a;border-radius:6px;font-size:14px;color:#444;padding:12px 16px}
.btn-submit{left:618px;top:4194px;width:96px;height:42px;border-radius:21px;background:var(--green);color:var(--white);font-size:14px;font-weight:700;display:flex;align-items:center;justify-content:center}
.info{position:absolute;left:779px;display:flex;align-items:center;gap:18px;font-size:14px;color:#555;line-height:22px}
.info-icon{width:36px;height:36px;border-radius:50%;border:1px solid #bbb;display:flex;align-items:center;justify-content:center;flex:none}
.social{left:780px;top:4202px;display:flex;gap:12px}
.social span{width:36px;height:36px;border-radius:50%;border:1px solid #bbb;display:block}
.foot-line{left:111px;top:4294px;width:975px;height:1px;background:var(--line)}
.copy{left:0;top:4332px;width:1200px;text-align:center;font-size:13px;color:#666}
</style>
</head>
<body>

<!-- Header -->
<div class="abs brand"><span class="brand-mark"></span><span class="brand-name">PetMind Studio</span></div>
<div class="abs call">
  <span class="call-icon"><svg width="22" height="22" viewBox="0 0 24 24"><path fill="#1c8a4c" d="M6.6 10.8a15.1 15.1 0 0 0 6.6 6.6l2.2-2.2a1 1 0 0 1 1-.25 11.4 11.4 0 0 0 3.6.57 1 1 0 0 1 1 1V20a1 1 0 0 1-1 1A17 17 0 0 1 3 4a1 1 0 0 1 1-1h3.5a1 1 0 0 1 1 1c0 1.25.2 2.45.57 3.57a1 1 0 0 1-.25 1z"/></svg></span>
  <span><small>Contact us on</small><strong>087 555 0148</strong></span>
</div>
<nav class="abs nav">
  <span class="active">Home</span><span>About</span><span>Canine &amp; Feline behaviour Consultancy</span><span>Equine Consultancy</span><span>Legal expert witness Consultancy</span><span>Education</span><span>Contact us</span>
</nav>
<div class="abs nav-line"></div>

<!-- Hero -->
<div class="abs hero" role="img" aria-label="Photo of a happy dog licking its nose against a green garden background"></div>
<h1 class="abs hero-title">Equine Training,<br>Performance &amp; Welfare</h1>
<div class="abs hero-rule"></div>
<ul class="abs hero-list">
  <li><svg width="18" height="18" viewBox="0 0 18 18"><circle cx="9" cy="9" r="9" fill="#fff"/><path d="M5 9.3l2.6 2.6L13 6.5" stroke="#1c8a4c" stroke-width="2.2" fill="none"/></svg>Understanding Animals</li>
  <li><svg width="18" height="18" viewBox="0 0 18 18"><circle cx="9" cy="9" r="9" fill="#fff"/><path d="M5 9.3l2.6 2.6L13 6.5" stroke="#1c8a4c" stroke-width="2.2" fill="none"/></svg>Improving animals lives through better understanding</li>
  <li><svg width="18" height="18" viewBox="0 0 18 18"><circle cx="9" cy="9" r="9" fill="#fff"/><path d="M5 9.3l2.6 2.6L13 6.5" stroke="#1c8a4c" stroke-width="2.2" fill="none"/></svg>Science-based, up-to-date relevant information regarding animal behaviour</li>
</ul>
<div class="abs btn-ghost">GET A QUOTE</div>
<div class="abs dots"><span class="on"></span><span></span><span></span><span></span></div>

<!-- Welcome -->
<h2 class="section-title" style="top:826px">Welcome to PetMind Studio</h2>
<div class="rule" style="top:902px"></div>
<p class="lead" style="top:938px">Animals have been used by humans for a variety of purposes, including as a source of food, for hunting, for mobility, to help win battles, for sport - and most recently, for companionship. Whether we are dog or cat lovers, horseriders or owners, through the course of our relationship with our animals, many of us</p>

<!-- Services band -->
<svg class="abs svc-band" width="1200" height="590" viewBox="0 0 1200 590" aria-hidden="true">
  <path d="M0 120 Q600 -60 1200 120 L1200 590 L0 590 Z" fill="#1c8a4c"/>
</svg>
<div class="svc-photo" role="img" aria-label="Photo of a boxer dog" style="left:117px;top:1168px;background:linear-gradient(160deg,#8a5a34,#3c2616)"></div>
<div class="svc-photo" role="img" aria-label="Photo of a golden retriever at a consultation" style="left:363px;top:1104px;background:linear-gradient(160deg,#e6e0d6,#b0743a)"></div>
<div class="svc-photo" role="img" aria-label="Photo of a rider on a horse in an arena" style="left:612px;top:1104px;background:linear-gradient(160deg,#dfe3e6,#4b4a45)"></div>
<div class="svc-photo" role="img" aria-label="Photo of a classroom lecture" style="left:864px;top:1168px;background:linear-gradient(160deg,#c9c2b6,#2f2e2c)"></div>

<div class="svc" style="left:103px;top:1414px"><h3>Behaviour<br>Consultations</h3><p>During a behaviour consultation, an individual assessment of the horse is carried out, incorporating information regarding</p></div>
<div class="svc" style="left:349px;top:1353px"><h3>Training<br>sessions</h3><p>Individual training sessions with horse and rider, designed to address training problems, the performance of problem</p></div>
<div class="svc" style="left:598px;top:1353px"><h3>Training your<br>horse</h3><p>This course incorporates both classroom sessions and practical sessions in the arena, developing the rider skills</p></div>
<div class="svc" style="left:850px;top:1414px"><h3>Training, performance<br>and welfare</h3><p>During this course, run for groups of 8 to 12, students will greatly deepen their understanding of the horse, through attending</p></div>
<div class="btn-svc" style="left:164px;top:1626px">READ MORE</div>
<div class="btn-svc" style="left:410px;top:1566px">READ MORE</div>
<div class="btn-svc" style="left:659px;top:1566px">READ MORE</div>
<div class="btn-svc" style="left:911px;top:1626px">READ MORE</div>

<!-- Components -->
<div class="abs components"></div>
<h2 class="section-title" style="top:1852px">Our Components</h2>
<div class="rule" style="top:1926px"></div>
<div class="abs comp-hub"><svg width="200" height="200" viewBox="0 0 200 200" aria-hidden="true"><circle cx="100" cy="100" r="88" fill="none" stroke="#fff" stroke-width="4"/></svg></div>

<div class="comp-icon" style="left:357px;top:2002px"><svg width="34" height="34" viewBox="0 0 24 24"><g fill="#1c8a4c"><ellipse cx="12" cy="16" rx="5" ry="4"/><circle cx="6" cy="10" r="2"/><circle cx="9.5" cy="6" r="2"/><circle cx="14.5" cy="6" r="2"/><circle cx="18" cy="10" r="2"/></g></svg></div>
<div class="comp-icon" style="left:357px;top:2148px"><svg width="34" height="34" viewBox="0 0 24 24"><g fill="none" stroke="#1c8a4c" stroke-width="2"><path d="M3 5h12v8H8l-3 3v-3H3z"/><path d="M17 9h4v8h-2v3l-3-3h-5v-2"/></g></svg></div>
<div class="comp-icon" style="left:749px;top:2002px"><svg width="34" height="34" viewBox="0 0 24 24"><g fill="#1c8a4c"><rect x="3" y="8" width="18" height="12" rx="2"/><path d="M9 8V5h6v3h-2V6.5h-2V8z"/></g></svg></div>
<div class="comp-icon" style="left:749px;top:2148px"><svg width="34" height="34" viewBox="0 0 24 24"><g fill="none" stroke="#1c8a4c" stroke-width="2"><path d="M12 3a6 6 0 0 0-3.5 10.9V17h7v-3.1A6 6 0 0 0 12 3z"/><path d="M9.5 20h5"/></g></svg></div>

<div class="comp-label right" style="left:17px;top:2022px"><h4>Small animal consultancy</h4><p>At vero eos et accumsan et ius</p></div>
<div class="comp-label right" style="left:17px;top:2168px"><h4>Equine behaviour consultancy</h4><p>At vero eos et accumsan et ius</p></div>
<div class="comp-label" style="left:866px;top:2022px"><h4>Legal case work</h4><p>At vero eos et accumsan et ius</p></div>
<div class="comp-label" style="left:866px;top:2168px"><h4>Education Provider</h4><p>At vero eos et accumsan et ius</p></div>

<!-- Equine -->
<h2 class="section-title" style="top:2450px">Equine Training, Performance and Welfare</h2>
<div class="rule" style="top:2527px"></div>
<p class="abs byline">Dr Aoife Brennan, Kilmore, Glenvar, Co Donegal.</p>
<p class="lead" style="top:2598px">Animals have been used by humans for a variety of purposes, including as a source of food, for hunting, for mobility, to help win battles, for sport - and most recently, for companionship. Whether we are dog or cat lovers, horseriders or owners, through the course of our relationship with our animals, many of us</p>
<div class="abs video" role="img" aria-label="Video still of a collie dog beside grazing horses"></div>
<div class="abs play"><svg width="26" height="26" viewBox="0 0 24 24"><path d="M7 4l13 8-13 8z" fill="#fff"/></svg></div>

<!-- Testimonials -->
<div class="abs testi" role="img" aria-label="Faded photo of a rider and horse in an arena"></div>
<h2 class="section-title" style="top:3252px">Client Testimonials</h2>
<div class="rule" style="top:3328px"></div>
<p class="abs quote">"Aoife has been coaching learners on the principles of equitation science as part of Meadowbrook Trust's Therapeutic Riding Coaching Programme and the Equine Assisted Learning Facilitator Training Programme since 2012. Her lectures continuously inspire and motivate learners to reconsider their approach to managing equines. Additionally, Aoife's approach provides a safe and non-judgemental environment in which learners can consider new ways of equine welfare and management"</p>
<p class="abs cite">Dr Niamh Walsh – Chief Executive Officer – Meadowbrook Trust</p>
<svg class="abs arrow" style="left:46px" width="24" height="36" viewBox="0 0 24 36" aria-hidden="true"><path d="M20 3L5 18l15 15" stroke="#777" stroke-width="3" fill="none"/></svg>
<svg class="abs arrow" style="left:1134px" width="24" height="36" viewBox="0 0 24 36" aria-hidden="true"><path d="M4 3l15 15L4 33" stroke="#777" stroke-width="3" fill="none"/></svg>

<!-- Contact -->
<h2 class="section-title" style="top:3766px">Contact Us</h2>
<div class="rule" style="top:3841px"></div>
<h3 class="abs col-title" style="left:111px;top:3906px">Contact form</h3>
<div class="field" style="left:111px;top:3969px;width:299px;height:44px">Name :</div>
<div class="field" style="left:419px;top:3969px;width:295px;height:44px">Phone no :</div>
<div class="field" style="left:111px;top:4031px;width:603px;height:44px">Email :</div>
<div class="field" style="left:111px;top:4092px;width:603px;height:85px">Message :</div>
<div class="abs btn-submit">SUBMIT</div>

<h3 class="abs col-title" style="left:779px;top:3906px">Contact Information</h3>
<div class="info" style="top:3960px"><span class="info-icon"><svg width="16" height="16" viewBox="0 0 24 24"><path fill="#1c8a4c" d="M12 2a7 7 0 0 0-7 7c0 5 7 13 7 13s7-8 7-13a7 7 0 0 0-7-7zm0 9.5A2.5 2.5 0 1 1 12 6.5a2.5 2.5 0 0 1 0 5z"/></svg></span><span>42 Harbour Road<br>Carndonagh</span></div>
<div class="info" style="top:4033px"><span class="info-icon"><svg width="16" height="16" viewBox="0 0 24 24"><path fill="#1c8a4c" d="M6.6 10.8a15.1 15.1 0 0 0 6.6 6.6l2.2-2.2a1 1 0 0 1 1-.25 11.4 11.4 0 0 0 3.6.57 1 1 0 0 1 1 1V20a1 1 0 0 1-1 1A17 17 0 0 1 3 4a1 1 0 0 1 1-1h3.5a1 1 0 0 1 1 1c0 1.25.2 2.45.57 3.57a1 1 0 0 1-.25 1z"/></svg></span><span>087 555 0148</span></div>
<div class="info" style="top:4097px"><span class="info-icon"><svg width="16" height="16" viewBox="0 0 24 24"><path fill="#1c8a4c" d="M3 5h18v14H3zm2 2v.5l7 5 7-5V7z"/></svg></span><span>hello@petmindstudio.ie</span></div>
<h3 class="abs col-title" style="left:779px;top:4152px">Social Media</h3>
<div class="abs social"><span></span><span></span><span></span></div>

<div class="abs foot-line"></div>
<p class="abs copy">Copyright © 2019, PetMind Studio. All rights reserved.</p>
<svg class="abs" style="left:1062px;top:4320px" width="30" height="18" viewBox="0 0 30 18" aria-hidden="true"><path d="M3 15L15 4l12 11" stroke="#999" stroke-width="2.5" fill="none"/></svg>

</body>
</html>
```